Wordpress Design Project - IT Consulting Services Web Site

Our are starting a new technology services company. We will provide services in software implementation and business intelligence.

We need a beautiful Wordpress web site design. We need a design for the homepage, and one interior content page.

The site must have a very professional and polished look and feel. What I have suggested below are things that I think work, but I am not a designer and I am open to your professional opinions. Please be willing to use your best judgment.

The homepage should have the following elements:
- A Header Area that includes:
o The company logo, and
o navigation (consistent with the interior page)
o a social media link section that includes rss feeds, youtube, facebook, linkedin and tweets
- A Body that includes:
o A slider
o An area that features up to six of the most recent or important posts including a thumbnail and small picture, a title, and a short excerpt for each.
o An area for around 100 words of text and an image
- A footer that includes:
o The company logo
o Contact information

The interior page is relatively simple. It should include the same navigation element as the homepage, and accommodate a one column text layout.

The current site …
You can visit the current site at www.plovernestworks.com I built the current site using the “Velkaro Swift Tap” premium theme. If you visit this site you get a sense of some of the things I am talking about, but there are things that I do not like about the current site. Here’s what I like and what I don’t like.

What I like about the current site:
- It is reactive – it adapts to the size of the viewing browser
- It has a “metro” feel to it. The company will have an association with Brintovax and having a “metro” theme is a plus, but not a requirement.
- It is different without being hard to navigate – the site the slider is from the “glide carousel plugin”, the posts are represented with tiles and rearrange themselves when a topic is selected.

What I don’t like:
- The site lacks a cohesive feel – it feels to me like a bunch of different elements without a single theme that pulls everything together.
- It is not aesthetically appealing to me.
- The tiles in the post section are too big.
- I don’t like the white background – I would prefer a background color and ideally a background that somehow incorporates the graphic in the logo.

About themes
As I said, I used a Velkaro theme in my design. I will be happy to continue using this theme, or would be willing to buy a new premium theme, so long as the cost is less than $100 U.S.

Site Map:
What we do
ERP Implementation
Business Intelligence
Who we are
What’s different about us
Principles
Mission, Vision, Values
Actions
How we work
What’s Different About Us
Blogs
What Papers
Presentations
Join
What we are looking for
What are you looking for?
Benefits
Context
Updates

Regarding Pictures
Please do not feel you need to use any of the pictures currently on the site.  Use whatever pictures you feel look best.  Comps are okay. 

It is not necessary to use any of the content on the current site - you do not need to use either the pictures or the text.  Please feel free to use pictures of your choice (comps okay), and/or lorem text.

The top level navigation is the navigation I would like.

Hello all,

Since this is a Wordpress project, it goes without saying I will need to implement this design in Wordpress.  It is not absolutely necessary that a design that matches an existing template (free or not), but a design that does will have an advantage over a design which requires that a new template be coded from scratch.

Thank you.

Target Market(s)

Business executives and potential employees

Industry/Entity Type

Software

Requirements
Nice to have
• It would be nice if the site was reactive.

```html
<!DOCTYPE html>
<html lang="en">
<head>
<meta charset="utf-8">
<title>Norvale Consulting – IT Consulting</title>
<link rel="stylesheet" href="https://fonts.googleapis.com/css2?family=Source+Sans+3:ital,wght@0,300;0,400;0,600;0,700;1,400&display=swap">
<style>
:root{
  --page-blue:#0ba2e5;
  --deep-blue:#1a80c6;
  --accent-blue:#1d9ad8;
  --ink:#222;
  --white:#fff;
  --header-top:#fdfdfd;
  --header-bottom:#dcdcdc;
  --social-grey:#8d8d8d;
  --brand-grey:#8a8a8a;
  --tile-green:#0a9e16;
  --tile-purple:#a314b6;
  --tile-orange:#d74b25;
  --rule-light:#7fd0f4;
}
*{box-sizing:border-box;margin:0;padding:0}
html,body{width:887px;height:1200px;overflow:hidden}
body{font-family:"Source Sans 3",Arial,sans-serif;background:var(--page-blue);color:var(--white);position:relative}
.abs{position:absolute}
a{color:inherit;text-decoration:none}

/* Header */
.site-header{left:0;top:0;width:887px;height:89px;background:linear-gradient(var(--header-top),var(--header-bottom));border-bottom:1px solid #bbb}
.brand{left:77px;top:48px;font-size:24px;font-weight:400;color:var(--brand-grey);letter-spacing:-.3px;white-space:nowrap}
.social{right:73px;top:8px;display:flex;gap:5px}
.social span{width:24px;height:24px;border-radius:50%;background:var(--social-grey)}
.main-nav{left:384px;top:57px;font-size:13px;color:#333}
.main-nav a{position:absolute;white-space:nowrap}

/* Hero */
.hero{left:0;top:90px;width:887px;height:344px;background:radial-gradient(circle at 72% 35%,#59c4f2 0,#1aa6ea 35%,#0b8fd8 100%);border-bottom:2px solid var(--white)}
.hero-photo{left:60px;top:0;width:440px;height:344px;background:radial-gradient(ellipse at 35% 50%,#e8d2c0 0,#b8c9d8 30%,#5ab8ec 70%,rgba(26,166,234,0) 100%)}
.hero-copy{left:524px;top:122px;width:270px}
.hero-kicker{font-size:20px;font-weight:700;line-height:24px}
.hero-title{font-size:30px;font-weight:300;line-height:34px;letter-spacing:-.5px;white-space:nowrap}
.hero-text{font-size:15px;line-height:18px;margin-top:6px}
.hero-more{font-size:12px;margin-top:14px;display:flex;align-items:center;gap:4px}
.hero-dots{left:720px;top:320px;display:flex;gap:6px}
.hero-dots span{width:13px;height:13px;background:#cfe9f7;border:1px solid #fff}
.hero-dots span.on{background:var(--deep-blue)}

/* Recent posts */
.posts-tab{left:74px;top:477px;width:163px;height:32px;background:var(--deep-blue);font-size:20px;font-weight:300;display:flex;align-items:center;gap:6px;padding-left:12px}
.posts-panel{left:74px;top:509px;width:459px;height:216px;background:var(--white);color:var(--ink)}
.post-tabs{left:8px;top:10px;width:448px;height:29px;display:flex;border-bottom:1px solid #e2e2e2}
.post-tabs span{flex:1;text-align:center;font-size:13px;line-height:28px;color:#555;border:1px solid #e2e2e2;border-bottom:none;border-left:none}
.post-tabs span:first-child{color:var(--accent-blue);border-left:1px solid #e2e2e2;background:#fff;border-bottom:1px solid #fff}
.post-card{left:8px;top:39px;width:448px;height:154px;border:1px solid #ececec;border-top:none}
.post-thumb{left:17px;top:27px;width:114px;height:106px;border:2px solid #ddd;background:linear-gradient(#eef2f6,#c9cfd6 60%,#3a3d45)}
.post-title{left:150px;top:22px;font-size:15px;font-weight:600;color:#111;white-space:nowrap}
.post-date{left:150px;top:42px;font-size:11px;color:#222}
.post-excerpt{left:150px;top:60px;width:282px;font-size:10.5px;line-height:15px;color:#666}
.post-button{left:150px;top:110px;width:60px;height:22px;background:var(--accent-blue);color:#fff;font-size:10.5px;text-align:center;line-height:22px}
.pager{display:flex;gap:2px}
.pager span{width:17px;height:15px;display:flex;align-items:center;justify-content:center}
.panel-pager{left:413px;top:197px}

/* Testimonials */
.testimonials-title{left:589px;top:476px;font-size:20px;color:#111;font-weight:400}
.testimonials-rule{left:589px;top:507px;width:225px;height:1px;background:var(--white)}
.testimonials-pager{left:776px;top:478px}
.quote{left:589px;top:538px;width:228px;font-size:12px;font-style:italic;line-height:18px}
.quote .mark{font-size:30px;font-weight:700;font-style:normal;color:#cfeafb;line-height:0;vertical-align:-10px}
.quote-name{left:710px;top:646px;font-size:11.5px;font-weight:700;color:#111}
.quote-role{left:600px;top:661px;width:213px;text-align:right;font-size:10px;color:#222}

.soft-rule{left:74px;top:762px;width:740px;height:1px;background:rgba(255,255,255,.2)}

/* Feature tiles */
.tile{top:792px;width:238px;height:148px}
.tile-green{left:74px;background:var(--tile-green)}
.tile-purple{left:325px;background:var(--tile-purple)}
.tile-orange{left:577px;background:var(--tile-orange)}
.tile-icon{left:14px;top:52px}
.tile-title{left:72px;top:26px;font-size:15px;font-weight:600}
.tile-text{left:72px;top:53px;width:158px;font-size:10.5px;line-height:15px}
.tile-more{left:72px;top:111px;font-size:10.5px}

/* Footer */
.footer-rule{left:74px;top:972px;width:740px;height:3px;background:var(--rule-light)}
.footer-head{font-size:15px;font-weight:400;color:#111;padding-bottom:2px;border-bottom:1px solid #fff}
.contact-head{left:77px;top:999px;width:174px}
.sitemap-head{left:306px;top:999px;width:174px}
.contact-lead{left:77px;top:1027px;font-size:14px;line-height:15px}
.contact-lead small{display:block;font-size:10.5px}
.contact-lines{left:77px;top:1061px;font-size:10px;line-height:14px}
.sitemap-col{top:1030px;font-size:9.5px;line-height:14.8px;list-style:none}
.sitemap-col li::before{content:"";display:inline-block;border-left:4px solid #fff;border-top:3px solid transparent;border-bottom:3px solid transparent;margin-right:4px}
.col-1{left:309px}.col-2{left:432px}.col-3{left:557px}
.footer-brand{left:701px;top:1103px;font-size:13px;font-weight:400;white-space:nowrap}
.bottom-rule{left:74px;top:1146px;width:740px;height:1px;background:rgba(255,255,255,.7)}
.copyright{left:0;top:1169px;width:887px;text-align:center;font-size:9.5px}
</style>
</head>
<body>

<header class="site-header abs">
  <div class="brand abs">Norvale Consulting</div>
  <div class="social abs" aria-label="Social links"><span></span><span></span><span></span><span></span><span></span></div>
  <nav class="main-nav abs">
    <a style="left:0">What we do</a>
    <a style="left:102px">Who we are</a>
    <a style="left:202px">How we work</a>
    <a style="left:313px">Join</a>
    <a style="left:374px">Contact Us</a>
  </nav>
</header>

<section class="hero abs">
  <div class="hero-photo abs" role="img" aria-label="Businessman touching a floating transparent screen showing a cloud"></div>
  <div class="hero-copy abs">
    <div class="hero-kicker">Lorem ipsum dolor sit</div>
    <div class="hero-title">AMET, CONSECTETUR</div>
    <div class="hero-text">Adipiscing elit. Nulla lobortis consequat mauris, eget eleifend nunc viverra viverra.</div>
    <div class="hero-more"><svg width="16" height="8" viewBox="0 0 16 8"><path d="M0 4h15M11 1l4 3-4 3" stroke="#fff" fill="none"/></svg>READ MORE</div>
  </div>
  <div class="hero-dots abs"><span></span><span class="on"></span><span></span></div>
</section>

<div class="posts-tab abs">
  <svg width="20" height="18" viewBox="0 0 20 18"><circle cx="6" cy="6" r="4" fill="#fff"/><path d="M0 18c0-5 3-7 6-7s6 2 6 7z" fill="#fff"/><ellipse cx="15" cy="4" rx="5" ry="3.5" fill="#fff"/></svg>
  Recent Posts
</div>
<section class="posts-panel abs">
  <div class="post-tabs abs"><span>Post 1</span><span>Post 2</span><span>Post 3</span><span>Post 4</span><span>Post 5</span><span>Post 6</span></div>
  <article class="post-card abs">
    <div class="post-thumb abs" role="img" aria-label="Portrait of a smiling businessman in a suit"></div>
    <div class="post-title abs">Lorem ipsum dolor sit amet, consectetur</div>
    <div class="post-date abs">17.06.2013</div>
    <p class="post-excerpt abs">Lorem ipsum dolor sit amet, consectetur adipiscing elit. Nulla lobortis consequat mauris, eget eleifend nunc viverra viverra. Ut ac risus odio.</p>
    <a class="post-button abs">Read More</a>
  </article>
  <div class="pager panel-pager abs">
    <span style="background:var(--accent-blue)"><svg width="6" height="8"><path d="M5 0L1 4l4 4" stroke="#fff" fill="none"/></svg></span>
    <span style="background:#ccc"><svg width="6" height="8"><path d="M1 0l4 4-4 4" stroke="#fff" fill="none"/></svg></span>
  </div>
</section>

<h2 class="testimonials-title abs">Testimonials</h2>
<div class="pager testimonials-pager abs">
  <span style="background:var(--deep-blue)"><svg width="6" height="8"><path d="M5 0L1 4l4 4" stroke="#fff" fill="none"/></svg></span>
  <span style="background:#fff"><svg width="6" height="8"><path d="M1 0l4 4-4 4" stroke="#1a80c6" fill="none"/></svg></span>
</div>
<div class="testimonials-rule abs"></div>
<blockquote class="quote abs"><span class="mark">&ldquo;</span> Lorem ipsum dolor sit amet, consectetur adipiscing elit. Nulla lobortis consequat mauris, eget eleifend nunc viverra viverra. Ut ac risus odio. Aliquam pretium purus sed nulla feugiat blandit..... <span class="mark">&rdquo;</span></blockquote>
<div class="quote-name abs">Lorem ipsum</div>
<div class="quote-role abs">Dolor sit amet, consectetur</div>

<div class="soft-rule abs"></div>

<article class="tile tile-green abs">
  <svg class="tile-icon abs" width="52" height="52" viewBox="0 0 52 52" fill="none" stroke="#fff" stroke-width="3"><rect x="2" y="16" width="30" height="22"/><path d="M8 24h16M8 30h12M10 44h16M18 38v6"/><circle cx="38" cy="16" r="12" fill="var(--tile-green)"/><path d="M38 4v12h12"/></svg>
  <h3 class="tile-title abs">Lorem ipsum dolor sit</h3>
  <p class="tile-text abs">consectetur adipiscing elit. Nulla l obortis consequat mauris, eget eleif-end nunc viverra viverra.</p>
  <a class="tile-more abs">&rarr; Read More</a>
</article>
<article class="tile tile-purple abs">
  <svg class="tile-icon abs" width="52" height="56" viewBox="0 0 52 56" fill="none" stroke="#fff" stroke-width="3"><circle cx="32" cy="8" r="6"/><circle cx="14" cy="18" r="5"/><path d="M4 34c0-8 5-11 10-11s10 3 10 11zM22 24c0-8 5-10 10-10s12 4 12 12c0 6-5 8-12 8"/><path d="M26 34v14M14 50h24"/></svg>
  <h3 class="tile-title abs">Lorem ipsum dolor sit</h3>
  <p class="tile-text abs">consectetur adipiscing elit. Nulla l obortis consequat mauris, eget eleif-end nunc viverra viverra.</p>
  <a class="tile-more abs">&rarr; Read More</a>
</article>
<article class="tile tile-orange abs">
  <svg class="tile-icon abs" width="46" height="46" viewBox="0 0 46 46" fill="none" stroke="#fff" stroke-width="3"><rect x="3" y="3" width="40" height="40" rx="2"/><circle cx="23" cy="23" r="11" stroke-width="2"/><path d="M12 23h22M23 12v22M15 16h16M15 30h16M23 12c-6 6-6 16 0 22M23 12c6 6 6 16 0 22" stroke-width="1.5"/></svg>
  <h3 class="tile-title abs">Lorem ipsum dolor sit</h3>
  <p class="tile-text abs">consectetur adipiscing elit. Nulla l obortis consequat mauris, eget eleif-end nunc viverra viverra.</p>
  <a class="tile-more abs">&rarr; Read More</a>
</article>

<footer>
  <div class="footer-rule abs"></div>
  <h4 class="footer-head contact-head abs">Contact information</h4>
  <div class="contact-lead abs">Lorem ipsum dolor sit amet,<small>adipiscing elit. Nulla lobortis consequat</small></div>
  <div class="contact-lines abs">Phone: 0000 000 0000<br>Fax: 0000 000 0000<br>Web: xxxxxxxxxxxxxxxx.com</div>
  <h4 class="footer-head sitemap-head abs">Site Map</h4>
  <ul class="sitemap-col col-1 abs"><li>What we do</li><li>ERP Implementation</li><li>Business Intelligence</li><li>Who we are</li><li>What's different about us</li><li>Principles</li></ul>
  <ul class="sitemap-col col-2 abs"><li>Mission, Vision, Values</li><li>Actions</li><li>How we work</li><li>What's Different About Us</li><li>Blogs</li><li>What Papers</li></ul>
  <ul class="sitemap-col col-3 abs"><li>Presentations</li><li>Join</li><li>What we are looking for</li><li>What are you looking for?</li><li>Benefits</li><li>Context</li></ul>
  <div class="footer-brand abs">Norvale Consulting</div>
  <div class="bottom-rule abs"></div>
  <div class="copyright abs">&copy; Copyright Information 2013. All Rights Reserved</div>
</footer>

</body>
</html>
```